Bathroom Renovation Business card design needed

Bathroom, Kitchen & Laundry Renovations
Mainly complete bathroom renovations

Target Market(s)

people wanting a total bathroom renovations and other trades people

Industry/Entity Type

Business

Contact Information for Business Card

Dalby Bathrooms
Tomas Dalby
Mobile: 0438 207615
Licence no: 764519K
Email: dalbybathrooms@mailnest.example

Logo styles of interest
Lettermark Logo
Requirements
Must have
• the business card should be predominantly blue
Nice to have
• the DB logo featured in the business card will be used on tshirts,tax invoices , letters etc so the DB will be the main feature, and preferably blue
Should not have
• We found the red DB logo through google images. We understand that it cannot be exactly the same but we like how the DB is linked. The example business card is something we designed but we prefer more blues. Maybe different shades of blue.

```html
<!DOCTYPE html>
<html lang="en">
<head>
<meta charset="utf-8">
<title>Dalby Bathrooms – Business Card</title>
<link rel="stylesheet" href="https://fonts.googleapis.com/css2?family=Baloo+2:wght@800&family=Arimo:wght@400&display=swap">
<style>
  :root {
    --card-white: #ffffff;
    --brand-blue: #1254a1;
    --band-blue: #4a86cc;
    --contact-blue: #80b0e3;
    --heading-font: "Baloo 2", sans-serif;
    --body-font: "Arimo", sans-serif;
  }
  html, body {
    margin: 0;
    padding: 0;
    overflow: hidden;
    background: var(--card-white);
  }
  .business-card {
    position: relative;
    width: 1200px;
    height: 693px;
    overflow: hidden;
    background: var(--card-white);
  }
  .card-background {
    position: absolute;
    inset: 0;
  }
  .wave-fill { fill: var(--brand-blue); }
  .wave-band { fill: var(--band-blue); }
  .brand-name {
    position: absolute;
    top: 88px;
    left: 0;
    width: 100%;
    margin: 0;
    text-align: center;
    font-family: var(--body-font);
    font-weight: 400;
    font-size: 60px;
    line-height: 72px;
    color: var(--brand-blue);
  }
  .card-details {
    position: absolute;
    top: 258px;
    left: 0;
    width: 100%;
    text-align: center;
  }
  .business-name {
    margin: 0;
    font-family: var(--heading-font);
    font-weight: 800;
    font-size: 66px;
    line-height: 76px;
    color: var(--card-white);
  }
  .person-name {
    margin: 8px 0 0;
    font-family: var(--body-font);
    font-weight: 400;
    font-size: 66px;
    line-height: 80px;
    color: var(--card-white);
  }
  .contact-list {
    list-style: none;
    margin: 26px 0 0;
    padding: 0;
    font-family: var(--body-font);
    font-weight: 400;
    font-size: 38px;
    color: var(--contact-blue);
  }
  .contact-list li { line-height: 62px; }
</style>
</head>
<body>
  <main class="business-card">
    <svg class="card-background" width="1200" height="693" viewBox="0 0 1200 693" aria-hidden="true">
      <path class="wave-band" d="M0,158 Q560,266 1200,122 L1200,693 L0,693 Z"/>
      <path class="wave-fill" d="M0,167 Q560,286 1200,141 L1200,693 L0,693 Z"/>
    </svg>

    <p class="brand-name">Dalby Bathrooms</p>

    <section class="card-details">
      <h1 class="business-name">Dalby Bathrooms</h1>
      <p class="person-name">Tomas Dalby</p>
      <ul class="contact-list">
        <li>Mobile: 0438 207615</li>
        <li>Email: dalbybathrooms@mailnest.example</li>
        <li>Licence no: 764519K</li>
      </ul>
    </section>
  </main>
</body>
</html>
```